" Serviços oferecidos 1. Palestras motivacionais para empresas ou instituições; 2. Atividade física e fisioterapia para populações especiais; a. Por necessidades especiais entende-se pessoas com doenças neurológicas (alzheimer, parkinson, etc), diabéticos, obesos, depressão, ansiedade, idosos). Além disso, se enquadram crianças e atletas da categoria master, que desejam participar de competições. 3. Massagem relaxante (quick massage, shiatsu), terapia manual, isostretching. "

```html
<!DOCTYPE html>
<html lang="pt-BR">
<head>
<meta charset="utf-8">
<title>Assinatura de e-mail – Neurovia</title>
<link href="https://fonts.googleapis.com/css2?family=Arimo:wght@400;700&display=swap" rel="stylesheet">
<style>
  :root {
    --teal: #1f4a4d;
    --orange: #d9781f;
    --ink: #1b1b1b;
    --muted: #666;
    --page: #ececec;
    --white: #ffffff;
    --soft: #f1f1f1;
  }
  * { margin: 0; padding: 0; box-sizing: border-box; }
  html, body { width: 1200px; height: 1200px; overflow: hidden; }
  body {
    background: var(--page);
    font-family: "Arimo", Arial, sans-serif;
    display: flex; align-items: center; justify-content: center;
  }
  .signature {
    width: 1080px; height: 232px;
    display: flex;
    box-shadow: 0 6px 18px rgba(0,0,0,.15);
  }
  .brand-panel {
    width: 452px; background: var(--teal);
    display: flex; align-items: center; justify-content: center;
  }
  .brand { display: flex; align-items: center; gap: 14px; color: var(--white); }
  .brand-dot { width: 34px; height: 34px; border-radius: 50%; background: var(--orange); }
  .brand-text { display: flex; flex-direction: column; }
  .brand-name { font-size: 50px; font-weight: 700; color: var(--white); line-height: 1; }
  .brand-tagline { font-size: 9px; letter-spacing: 2px; color: #b9c9ca; text-transform: uppercase; margin-top: 6px; }
  .info-panel {
    position: relative; flex: 1;
    background: linear-gradient(90deg, var(--white) 0%, var(--soft) 100%);
    padding: 36px 0 0 70px;
  }
  .accent-tab {
    position: absolute; left: 0; top: 0;
    width: 18px; height: 126px;
    background: var(--orange);
    border-radius: 0 10px 10px 0;
  }
  .person-name { font-size: 25px; font-weight: 700; color: var(--ink); }
  .person-role { font-size: 10px; font-weight: 700; color: var(--muted); margin: 4px 0 0 70px; }
  .contact-row { display: flex; align-items: flex-start; gap: 12px; margin-top: 18px; font-size: 17px; font-weight: 700; color: var(--ink); }
  .contact-row.phone { font-size: 14px; line-height: 1.25; margin-top: 14px; }
  .icon { width: 18px; height: 18px; flex: none; }
  .social-row { display: flex; align-items: center; gap: 12px; margin-top: 12px; font-size: 17px; font-weight: 700; color: var(--ink); }
  .social-mark { width: 16px; height: 16px; background: var(--teal); border-radius: 3px; }
  .social-mark.alt { background: var(--orange); margin-left: 26px; }
</style>
</head>
<body>
  <section class="signature">
    <div class="brand-panel">
      <div class="brand">
        <span class="brand-dot"></span>
        <div class="brand-text">
          <span class="brand-name">Neurovia</span>
          <span class="brand-tagline">saúde em movimento</span>
        </div>
      </div>
    </div>
    <div class="info-panel">
      <span class="accent-tab"></span>
      <p class="person-name">Nome Sobrenome</p>
      <p class="person-role">FUNÇÃO</p>
      <div class="contact-row">
        <svg class="icon" viewBox="0 0 18 18"><rect x="1" y="2" width="16" height="14" rx="2" fill="#1b1b1b"/><rect x="4" y="5.5" width="10" height="7" fill="#fff"/></svg>
        <span>nome@movimento.com.br</span>
      </div>
      <div class="contact-row phone">
        <svg class="icon" viewBox="0 0 18 18"><rect x="1" y="1" width="16" height="16" rx="2" fill="#1b1b1b"/><path d="M5 6c0-1 1-2 2-2l1 2-1 1c.5 1.5 1.5 2.5 3 3l1-1 2 1c0 1-1 2-2 2-3 0-6-3-6-6z" fill="#fff"/></svg>
        <span>+55 (11) 5012-3040 / Ramal: 2210<br>+55 (11) 98123-4567</span>
      </div>
      <div class="social-row">
        <span class="social-mark"></span><span>empresa</span>
        <span class="social-mark alt"></span><span>@empresa</span>
      </div>
    </div>
  </section>
</body>
</html>
```